RevelHubQZ Business Cards

Front
Has logo with a design. Website address (www.revelhubqz.example)
Has slogan (discover nightlife)
Has phone number (5129873304)
Should be bold and stands out.

Back
Has details about what we offer.

Events
Search upcoming events
Submit events
Party Image Gallery
View and download HQ party images
Sign up as a contributing event photographer and get paid!
Tickets
Sell your event tickets online for free!
Direct pay
No ticket fee

Target Market(s)

These cards will be handed out in clubs and events to patrons.

Industry/Entity Type

Business

Contact Information for Business Card

Should match or mirror our website in some sort of way. Visit the website to get ideas.

Requirements
Must have
• Must be designed for a 3x3 inch card.

```html
<!DOCTYPE html>
<html lang="en">
<head>
<meta charset="utf-8">
<title>RevelHubQZ Business Cards</title>
<link href="https://fonts.googleapis.com/css2?family=Open+Sans:wght@400;600;700&display=swap" rel="stylesheet">
<style>
  :root {
    --stage: #2e303d;
    --pink: #e04397;
    --blue: #35a6dc;
    --white: #ffffff;
    --ink: #1c1c1c;
    --card-shadow: 0 14px 40px rgba(0, 0, 0, 0.45);
  }
  * { margin: 0; padding: 0; box-sizing: border-box; }
  html, body {
    width: 1200px;
    height: 1160px;
    overflow: hidden;
    background: var(--stage);
    font-family: "Open Sans", Arial, sans-serif;
  }
  .card {
    position: absolute;
    top: 334px;
    width: 501px;
    height: 501px;
    overflow: hidden;
    box-shadow: var(--card-shadow);
  }
  .card--back { left: 42px; background: var(--pink); color: var(--white); }
  .card--front { left: 657px; background: var(--white); }

  .brand { position: absolute; display: flex; align-items: center; gap: 14px; }
  .brand__dot { width: 46px; height: 46px; border-radius: 50%; flex: none; }
  .brand__name { font-weight: 600; font-size: 40px; letter-spacing: -1px; line-height: 1; }
  .brand__slogan {
    position: absolute;
    font-size: 14px;
    letter-spacing: 7px;
    white-space: nowrap;
  }

  .card--back .brand { left: 27px; top: 128px; }
  .card--back .brand__dot { background: var(--white); }
  .card--back .brand__name { color: var(--white); }
  .card--back .brand__slogan { left: 87px; top: 178px; color: var(--white); }

  .offer { position: absolute; left: 27px; }
  .offer--events { top: 254px; }
  .offer--tickets { top: 345px; }
  .offer__title { font-weight: 700; font-size: 16.5px; line-height: 22px; }
  .offer__line { font-size: 14.5px; line-height: 19px; letter-spacing: 0.3px; }

  .card--front .brand { left: 24px; top: 46px; }
  .card--front .brand__dot { background: var(--blue); }
  .card--front .brand__name { color: var(--blue); }
  .card--front .brand__slogan { left: 123px; top: 100px; color: var(--ink); font-size: 13px; letter-spacing: 6px; }

  .person { position: absolute; right: 21px; top: 220px; text-align: right; color: var(--ink); }
  .person__name { font-weight: 700; font-size: 25px; letter-spacing: 1px; line-height: 30px; }
  .person__role { font-size: 18px; line-height: 22px; letter-spacing: 0.5px; }
  .divider { position: absolute; left: 21px; right: 21px; top: 276px; height: 4px; background: var(--blue); }

  .contacts { position: absolute; left: 24px; top: 318px; list-style: none; color: var(--ink); }
  .contacts li { display: flex; align-items: center; gap: 12px; height: 32px; font-size: 17px; letter-spacing: 0.3px; }
  .contacts svg { width: 18px; height: 18px; flex: none; }

  .wave { position: absolute; left: 0; bottom: 0; width: 501px; height: 501px; }
</style>
</head>
<body>

<section class="card card--back" aria-label="Card back">
  <div class="brand">
    <span class="brand__dot"></span>
    <span class="brand__name">RevelHubQZ</span>
  </div>
  <span class="brand__slogan">discover nightlife</span>

  <div class="offer offer--events">
    <h2 class="offer__title">Events</h2>
    <p class="offer__line">Search Upcoming Events | Submit Events | Party Image Gallery</p>
    <p class="offer__line">View &amp; Download HQ Party Images</p>
  </div>

  <div class="offer offer--tickets">
    <h2 class="offer__title">Tickets</h2>
    <p class="offer__line">Sell Your Event Tickets Online For Free | Direct Pay</p>
    <p class="offer__line">No Ticket Fee</p>
  </div>
</section>

<section class="card card--front" aria-label="Card front">
  <div class="brand">
    <span class="brand__dot"></span>
    <span class="brand__name">RevelHubQZ</span>
  </div>
  <span class="brand__slogan">discover nightlife</span>

  <div class="person">
    <p class="person__name">Mara Quill</p>
    <p class="person__role">Director</p>
  </div>
  <div class="divider"></div>

  <ul class="contacts">
    <li>
      <svg viewBox="0 0 24 24" aria-hidden="true"><path fill="#e04397" d="M6.6 10.8a15.1 15.1 0 0 0 6.6 6.6l2.2-2.2c.3-.3.7-.4 1-.2 1.1.4 2.3.6 3.6.6.6 0 1 .4 1 1V20c0 .6-.4 1-1 1A17 17 0 0 1 3 4c0-.6.4-1 1-1h3.5c.6 0 1 .4 1 1 0 1.3.2 2.5.6 3.6.1.3 0 .7-.2 1z"/></svg>
      <span>5129873304</span>
    </li>
    <li>
      <svg viewBox="0 0 24 24" aria-hidden="true"><rect x="2" y="5" width="20" height="14" fill="none" stroke="#e04397" stroke-width="2.2"/><path d="M2 5l10 8 10-8M2 19l7-7M22 19l-7-7" fill="none" stroke="#e04397" stroke-width="2"/></svg>
      <span>info@revelhubqz.example</span>
    </li>
    <li>
      <svg viewBox="0 0 24 24" aria-hidden="true"><g fill="none" stroke="#e04397" stroke-width="1.6"><circle cx="12" cy="12" r="9.5"/><ellipse cx="12" cy="12" rx="4" ry="9.5"/><path d="M2.5 12h19M4 7h16M4 17h16"/></g></svg>
      <span>www.revelhubqz.example</span>
    </li>
  </ul>

  <svg class="wave" viewBox="0 0 501 501" aria-hidden="true">
    <path fill="#e04397" d="M0 438 C70 410 150 405 220 424 C290 444 330 478 400 476 C440 475 475 466 501 457 L501 501 L0 501 Z"/>
    <path fill="none" stroke="#35a6dc" stroke-width="3" d="M130 413 C200 414 250 440 300 462 C340 478 370 480 400 478"/>
  </svg>
</section>

</body>
</html>
```